Need a website for our company

We need a website for our company to showcase all our work for customers to see.
We do all phases of home improvement:
Dormers/Extensions
Basement Remodel
Masonry/Concrete/Pavers/Asphalt
Cultured Stone Veneer
Kitchens
Bathrooms
Pool designs
Outdoor Bathroom
Outdoor Kitchens
Tile work
For reference, something similar to this website: https://brightoakrenovations.example/
Target Market(s)
We are trying to target homeowners.
Coding
Number of Pages Required
Look and feel

```html
<!DOCTYPE html>
<html lang="en">
<head>
<meta charset="utf-8">
<title>Brightoak Renovations Co.</title>
<link href="https://fonts.googleapis.com/css2?family=Poppins:wght@300;400;500;600&display=swap" rel="stylesheet">
<style>
:root{
  --black:#000;
  --ink:#111;
  --text:#222;
  --muted:#555;
  --line:#cfcfcf;
  --panel:#f3f3f3;
  --white:#fff;
  --footer:#121212;
  --footer-box:#1d1d1d;
}
*{box-sizing:border-box;margin:0;padding:0}
html,body{width:1200px;height:2973px;overflow:hidden;background:var(--white)}
body{font-family:'Poppins',sans-serif;color:var(--text);position:relative}
.abs{position:absolute}
.topbar{left:0;top:0;width:1200px;height:122px;background:var(--black);color:var(--white)}
.brand{font-weight:600;letter-spacing:.5px;font-size:12px;display:flex;align-items:center;gap:8px}
.brand .mark{width:14px;height:14px;border:1.5px solid currentColor}
.contact{display:flex;align-items:center;gap:12px;top:46px}
.contact .ic{width:36px;height:36px;border-radius:50%;background:#d9d9d9;display:flex;align-items:center;justify-content:center}
.contact small{display:block;font-size:11px;color:#bbb}
.contact b{font-size:13px;font-weight:600}
.vsep{top:34px;width:1px;height:56px;background:#2a2a2a}
.nav{top:122px;left:0;width:1200px;height:59px}
.nav a{position:absolute;top:22px;font-size:12px;font-weight:500;color:var(--ink);text-decoration:none}
.nav .under{left:105px;top:55px;width:32px;height:2px;background:var(--ink)}
.soc{top:140px;width:24px;height:24px;border-radius:50%;background:#eee}
.btn-est{left:918px;top:134px;width:177px;height:36px;border-radius:18px;background:var(--black);color:var(--white);font-size:13px;font-weight:500;display:flex;align-items:center;justify-content:center}
.hero{left:105px;top:181px;width:990px;height:547px;background:radial-gradient(ellipse at 40% 55%,#5a5046 0%,#2f2a25 45%,#141210 100%)}
.hero-c{left:105px;top:181px;width:990px;text-align:center;color:var(--white)}
.hero-c .tag{position:absolute;top:146px;width:100%;font-size:9px;letter-spacing:.5px}
.hero-c h1{position:absolute;top:172px;width:100%;font-size:37px;font-weight:500;line-height:46px}
.hero-btn{left:500px;top:528px;width:198px;height:40px;border-radius:20px;background:#ddd;color:var(--ink);font-size:13px;font-weight:500;display:flex;align-items:center;justify-content:center}
.dot{top:672px;width:6px;height:6px;border-radius:50%;background:#fff}
.exp-play{left:164px;top:791px;width:48px;height:48px;border-radius:50%;background:#1a1a1a;display:flex;align-items:center;justify-content:center}
.exp-sm{left:224px;top:790px;font-size:11px}
.exp-big{left:224px;top:804px;font-size:29px;font-weight:500;color:var(--ink)}
.exp-q{left:600px;top:777px;width:460px;font-size:11px;line-height:18px}
.exp-name{left:600px;top:817px;font-size:14px;font-weight:600;color:var(--ink)}
.exp-role{left:600px;top:836px;font-size:8px;font-weight:500}
.rule{left:105px;width:990px;height:2px;background:var(--ink)}
.rule::before,.rule::after{content:"";position:absolute;top:-3px;width:2px;height:8px;background:var(--ink)}
.rule::before{left:0}.rule::after{right:0}
h2.sec{font-size:20px;font-weight:500;color:var(--ink)}
.grid{left:105px;top:976px;width:990px;display:grid;grid-template-columns:repeat(5,185px);column-gap:16px;row-gap:20px}
.tile .ph{height:112px}
.tile p{font-size:9px;font-weight:500;margin-top:10px;color:var(--ink)}
.why{left:0;top:1314px;width:1200px;height:339px;background:var(--panel)}
.why h3{font-size:19px;font-weight:600;color:var(--ink)}
.why p{font-size:11px;line-height:18px}
.feat h4{font-size:14px;font-weight:500;color:var(--ink);margin-bottom:6px}
.feat p{font-size:11px;line-height:18px;width:250px}
.stat{top:1701px;width:277px;height:160px;border:1px solid #ccc;padding:20px 22px}
.stat .ic{position:absolute;left:18px;top:22px;width:40px;height:40px;border-radius:50%;border:1px solid #ccc;display:flex;align-items:center;justify-content:center}
.stat .num{position:absolute;left:71px;top:14px;font-size:41px;font-weight:300;color:var(--ink)}
.stat h4{position:absolute;left:22px;top:74px;font-size:15px;font-weight:500;color:var(--ink)}
.stat p{position:absolute;left:22px;top:105px;font-size:11px;line-height:18px;width:230px}
.card{top:1994px;width:316px;height:374px;background:var(--panel);text-align:center}
.card .stars{margin-top:42px;font-size:9px;letter-spacing:3px;color:#888}
.card .q{margin:12px auto 0;width:235px;font-size:10.5px;line-height:19.5px}
.card .av{position:absolute;left:131px;top:246px;width:54px;height:54px;border-radius:50%;background:linear-gradient(#8a7d72,#4a3f38)}
.card b{position:absolute;left:0;width:100%;top:306px;font-size:11px;font-weight:600;color:var(--ink)}
.card small{position:absolute;left:0;width:100%;top:320px;font-size:9px}
.arr{top:2140px;width:30px;height:30px;background:#3a3a3a;display:flex;align-items:center;justify-content:center}
.footer{left:0;top:2452px;width:1200px;height:389px;background:var(--footer);color:var(--white)}
.footer h5{font-size:14px;font-weight:500}
.footer ul{list-style:none}
.footer li{font-size:12px;height:25.4px;display:flex;align-items:center;gap:8px;color:#ddd}
.footer li svg{flex:none}
.news{left:428px;top:2693px;width:662px;height:113px;border-radius:14px;background:var(--footer-box)}
.inp{left:768px;top:2725px;width:283px;height:49px;border-radius:25px;background:var(--white);color:#777;font-size:12px;padding-left:22px;display:flex;align-items:center}
.send{left:1005px;top:2730px;width:40px;height:40px;border-radius:50%;background:var(--black);display:flex;align-items:center;justify-content:center}
.copy{left:0;top:2841px;width:1200px;height:68px;background:var(--black);color:#ccc;font-size:10px;padding:28px 105px}
</style>
</head>
<body>

<header class="abs topbar">
  <div class="abs brand" style="left:136px;top:54px;color:#eee"><span class="mark"></span>BRIGHTOAK RENOVATIONS CO.</div>
  <div class="abs contact" style="left:480px">
    <span class="ic"><svg width="16" height="16" viewBox="0 0 24 24"><path d="M6.6 10.8a15 15 0 006.6 6.6l2.2-2.2c.3-.3.7-.4 1-.2 1.1.4 2.3.6 3.6.6.6 0 1 .4 1 1V20c0 .6-.4 1-1 1A17 17 0 013 4c0-.6.4-1 1-1h3.5c.6 0 1 .4 1 1 0 1.3.2 2.5.6 3.6.1.3 0 .7-.2 1z" fill="#333"/></svg></span>
    <div><small>Call</small><b>555 014 2290</b></div>
  </div>
  <div class="abs vsep" style="left:641px"></div>
  <div class="abs contact" style="left:664px">
    <span class="ic"><svg width="16" height="16" viewBox="0 0 24 24"><path d="M3 6h18v12H3z" fill="#333"/><path d="M3 6l9 7 9-7" stroke="#d9d9d9" stroke-width="1.6" fill="none"/></svg></span>
    <div><small>Email</small><b>hello@brightoak.example</b></div>
  </div>
  <div class="abs vsep" style="left:863px"></div>
  <div class="abs contact" style="left:897px">
    <span class="ic"><svg width="16" height="16" viewBox="0 0 24 24"><path d="M12 2a7 7 0 00-7 7c0 5 7 13 7 13s7-8 7-13a7 7 0 00-7-7zm0 9.5a2.5 2.5 0 110-5 2.5 2.5 0 010 5z" fill="#333"/></svg></span>
    <div><small>Address</small><b>48 Maple Row, USA</b></div>
  </div>
</header>

<nav class="abs nav">
  <a style="left:105px">Home</a>
  <a style="left:173px">About Us</a>
  <a style="left:260px">Features</a>
  <a style="left:346px">Services</a>
  <a style="left:429px">Projects</a>
  <a style="left:512px">Contacts</a>
  <span class="abs under"></span>
</nav>
<span class="abs soc" style="left:781px"></span>
<span class="abs soc" style="left:815px"></span>
<span class="abs soc" style="left:848px"></span>
<span class="abs soc" style="left:882px"></span>
<div class="abs btn-est">Get A Free Estimate</div>

<div class="abs hero" role="img" aria-label="Dimly lit living room with a sofa, a woman relaxing and a table lamp"></div>
<div class="abs hero-c">
  <div class="tag">HOME RENOVATIONS</div>
  <h1>Let's Build Your<br>Dream House<br>Together With Us</h1>
</div>
<div class="abs hero-btn">Make An Appoinment</div>
<span class="abs dot" style="left:573px;border:1.5px solid #fff;background:none;width:8px;height:8px;top:671px"></span>
<span class="abs dot" style="left:590px"></span>
<span class="abs dot" style="left:606px"></span>
<span class="abs dot" style="left:623px"></span>

<div class="abs exp-play"><svg width="18" height="18" viewBox="0 0 24 24"><path d="M5 3l16 9-16 9 4-9z" fill="#fff"/></svg></div>
<div class="abs exp-sm">Custom Building &amp; Home Renovations</div>
<div class="abs exp-big">30 Years Of Experience</div>
<p class="abs exp-q">Lorem ipsum dolor sit amet, consectetur adipiscing elit. Mauris vehicula metus eget tempor dapibus. Aliquam elit est, dignissim eu erat a, dignissim mollis sapien.</p>
<div class="abs exp-name">Helena R. Marsh</div>
<div class="abs exp-role">EXECUTIVE DIRECTOR</div>

<div class="abs rule" style="top:898px"></div>
<h2 class="abs sec" style="left:105px;top:913px">Home Improvement A-Z</h2>

<section class="abs grid">
  <div class="tile"><div class="ph" role="img" aria-label="Large house with dormers among trees" style="background:linear-gradient(#5f7a4a,#8a8a78 60%,#3d4a30)"></div><p>Dormers/Extensions</p></div>
  <div class="tile"><div class="ph" role="img" aria-label="Remodelled basement parking area" style="background:linear-gradient(#3c4448,#7b8488)"></div><p>Basement Remodel</p></div>
  <div class="tile"><div class="ph" role="img" aria-label="Stone paver garden path" style="background:linear-gradient(120deg,#8b7466,#a8948a 60%,#5e6e3a)"></div><p>Masonry/Concrete/Pavers/Asphalt</p></div>
  <div class="tile"><div class="ph" role="img" aria-label="Carved stone columns" style="background:linear-gradient(#b7ab9c,#857868)"></div><p>Cultured Stone Veneer</p></div>
  <div class="tile"><div class="ph" role="img" aria-label="Bright white kitchen with wood island" style="background:linear-gradient(#ececec,#c9b49a)"></div><p>Kitchens</p></div>
  <div class="tile"><div class="ph" role="img" aria-label="Wood panelled bathroom with stone basin" style="background:linear-gradient(#8a5a30,#4a3a2a)"></div><p>Bathrooms</p></div>
  <div class="tile"><div class="ph" role="img" aria-label="Turquoise swimming pool with deck" style="background:linear-gradient(120deg,#a77a50,#3cc0c8 50%,#6fd6dc)"></div><p>Pool designs</p></div>
  <div class="tile"><div class="ph" role="img" aria-label="Row of blue outdoor toilet cabins" style="background:linear-gradient(#3a6a7a,#1e5060)"></div><p>Outdoor Bathroom</p></div>
  <div class="tile"><div class="ph" role="img" aria-label="Covered outdoor kitchen patio" style="background:linear-gradient(#4a4038,#8a7a66)"></div><p>Outdoor Kitchens</p></div>
  <div class="tile"><div class="ph" role="img" aria-label="Hands working with a tile tool" style="background:linear-gradient(120deg,#1e3050,#c08060 60%,#f0f0f0)"></div><p>Tile work</p></div>
</section>

<section class="abs why">
  <h3 class="abs" style="left:104px;top:52px">WHY CHOOSE US ?</h3>
  <p class="abs" style="left:106px;top:97px;width:330px">Lorem ipsum dolor sit amet, consectetur adipiscing elit. Mauris vehicula metus eget tempor dapibus. Aliquam elit est, dignissim eu erat a, dignissim mollis sapien.</p>
  <h3 class="abs" style="left:542px;top:52px;font-weight:500">Concept To Creation Perfect Form &amp; Function</h3>
  <div class="abs feat" style="left:542px;top:114px"><h4>01. No Hidden Cost</h4><p>Lorem ipsum dolor sit amet, consectetur adipiscing elit.</p></div>
  <div class="abs feat" style="left:839px;top:114px"><h4>02. Prompt Customer Service</h4><p>Mauris vehicula metus eget tempor dapibus. Aliquam elit est, dignissim eu erat.</p></div>
  <div class="abs" style="left:542px;top:201px;width:553px;height:1px;background:#9a9a9a"></div>
  <div class="abs feat" style="left:542px;top:230px"><h4>03. Guaranteed Personal Service</h4><p>Lorem ipsum dolor sit amet, consectetur adipiscing elit.</p></div>
  <div class="abs feat" style="left:839px;top:230px"><h4>04. Guaranteed Personal Service</h4><p>Mauris vehicula metus eget tempor dapibus. Aliquam elit est, dignissim eu erat.</p></div>
</section>

<div class="abs stat" style="left:156px">
  <span class="ic"><svg width="18" height="18" viewBox="0 0 24 24" fill="none" stroke="#555" stroke-width="1.4"><path d="M21 3L3 10l7 3 3 7z"/><path d="M10 13l11-10"/></svg></span>
  <span class="num">45K</span><h4>Project Renovate</h4><p>Lorem ipsum dolor sit amet, consectetur adipiscing elit.</p>
</div>
<div class="abs stat" style="left:455px">
  <span class="ic"><svg width="18" height="18" viewBox="0 0 24 24" fill="none" stroke="#555" stroke-width="1.4"><path d="M12 20s-8-5-8-11a4 4 0 018-1 4 4 0 018 1c0 6-8 11-8 11z"/></svg></span>
  <span class="num">100%</span><h4>Project Renovate</h4><p>Lorem ipsum dolor sit amet, consectetur adipiscing elit.</p>
</div>
<div class="abs stat" style="left:754px">
  <span class="ic"><svg width="18" height="18" viewBox="0 0 24 24" fill="none" stroke="#555" stroke-width="1.4"><path d="M3 11l9-8 9 8M5 9v12h14V9M10 21v-6h4v6"/></svg></span>
  <span class="num">1,500</span><h4>Project Renovate</h4><p>Lorem ipsum dolor sit amet, consectetur adipiscing elit.</p>
</div>

<div class="abs rule" style="top:1910px"></div>
<h2 class="abs sec" style="left:0;width:1194px;text-align:center;top:1930px">Testimonials</h2>

<div class="abs arr" style="left:0"><svg width="12" height="12" viewBox="0 0 24 24" fill="none" stroke="#fff" stroke-width="2"><path d="M20 12H4M10 6l-6 6 6 6"/></svg></div>
<div class="abs arr" style="left:1170px"><svg width="12" height="12" viewBox="0 0 24 24" fill="none" stroke="#fff" stroke-width="2"><path d="M4 12h16M14 6l6 6-6 6"/></svg></div>

<article class="abs card" style="left:105px">
  <div class="stars">★★★★★</div>
  <p class="q">In non velit pharetra augue pharetra vulputate. Vestibulum nunc orci, finibus sit amet odio egestas, pharetra pretium odio. Donec mi metus, hendrerit sit amet tortor ac, gravida laoreet metus. Aenean ut gravida augue, in mollis eros. Nam suscipit, libero at iaculis hendrerit, ex erat varius erat, ut elementum mi augue ac elit.</p>
  <span class="av" role="img" aria-label="Customer portrait"></span><b>Daniel Roper</b><small>Our Customer</small>
</article>
<article class="abs card" style="left:442px">
  <div class="stars">★★★★★</div>
  <p class="q">In non velit pharetra augue pharetra vulputate. Vestibulum nunc orci, finibus sit amet odio egestas, pharetra pretium odio. Donec mi metus, hendrerit sit amet tortor ac, gravida laoreet metus. Aenean ut gravida augue, in mollis eros. Nam suscipit, libero at iaculis hendrerit, ex erat varius erat, ut elementum mi augue ac elit.</p>
  <span class="av" role="img" aria-label="Customer portrait"></span><b>Nadia Fields</b><small>Our Customer</small>
</article>
<article class="abs card" style="left:779px">
  <div class="stars">★★★★★</div>
  <p class="q">In non velit pharetra augue pharetra vulputate. Vestibulum nunc orci, finibus sit amet odio egestas, pharetra pretium odio. Donec mi metus, hendrerit sit amet tortor ac, gravida laoreet metus. Aenean ut gravida augue, in mollis eros. Nam suscipit, libero at iaculis hendrerit, ex erat varius erat, ut elementum mi augue ac elit.</p>
  <span class="av" role="img" aria-label="Customer portrait"></span><b>Owen Carter</b><small>Our Customer</small>
</article>

<footer class="abs footer">
  <div class="abs brand" style="left:112px;top:84px;color:#ddd"><span class="mark"></span>BRIGHTOAK RENOVATIONS CO.</div>
  <p class="abs" style="left:105px;top:147px;width:215px;font-size:12px;line-height:18px;color:#ddd">Sed ut perspiciatis unde omnis iste natus feria delavirot voluptatem accusantium.</p>
  <div class="abs" style="left:105px;top:217px;width:230px;height:1px;background:#333"></div>
  <h5 class="abs" style="left:106px;top:240px">Social Media</h5>
  <span class="abs" style="left:105px;top:276px;width:28px;height:28px;border-radius:50%;background:#ddd"></span>
  <span class="abs" style="left:146px;top:276px;width:28px;height:28px;border-radius:50%;background:#ddd"></span>
  <span class="abs" style="left:187px;top:276px;width:28px;height:28px;border-radius:50%;background:#ddd"></span>
  <span class="abs" style="left:228px;top:276px;width:28px;height:28px;border-radius:50%;background:#ddd"></span>

  <h5 class="abs" style="left:427px;top:53px">Quick Links</h5>
  <ul class="abs" style="left:427px;top:83px">
    <li><svg width="8" height="10" viewBox="0 0 8 12" fill="none" stroke="#fff" stroke-width="1.5"><path d="M1 1l5 5-5 5"/></svg>HOME</li>
    <li><svg width="8" height="10" viewBox="0 0 8 12" fill="none" stroke="#fff" stroke-width="1.5"><path d="M1 1l5 5-5 5"/></svg>ABOUT US</li>
    <li><svg width="8" height="10" viewBox="0 0 8 12" fill="none" stroke="#fff" stroke-width="1.5"><path d="M1 1l5 5-5 5"/></svg>FEATURES</li>
    <li><svg width="8" height="10" viewBox="0 0 8 12" fill="none" stroke="#fff" stroke-width="1.5"><path d="M1 1l5 5-5 5"/></svg>SERVICES</li>
    <li><svg width="8" height="10" viewBox="0 0 8 12" fill="none" stroke="#fff" stroke-width="1.5"><path d="M1 1l5 5-5 5"/></svg>PROJECTS</li>
  </ul>
  <h5 class="abs" style="left:659px;top:53px">Support Links</h5>
  <ul class="abs" style="left:657px;top:83px">
    <li><svg width="8" height="10" viewBox="0 0 8 12" fill="none" stroke="#fff" stroke-width="1.5"><path d="M1 1l5 5-5 5"/></svg>Privacy Policy</li>
    <li><svg width="8" height="10" viewBox="0 0 8 12" fill="none" stroke="#fff" stroke-width="1.5"><path d="M1 1l5 5-5 5"/></svg>Terms &amp; Conditions</li>
    <li><svg width="8" height="10" viewBox="0 0 8 12" fill="none" stroke="#fff" stroke-width="1.5"><path d="M1 1l5 5-5 5"/></svg>Support</li>
    <li><svg width="8" height="10" viewBox="0 0 8 12" fill="none" stroke="#fff" stroke-width="1.5"><path d="M1 1l5 5-5 5"/></svg>Disclaimer</li>
  </ul>
  <h5 class="abs" style="left:898px;top:53px">Support Links</h5>
  <ul class="abs" style="left:893px;top:83px">
    <li><svg width="10" height="12" viewBox="0 0 24 24"><path d="M12 2a7 7 0 00-7 7c0 5 7 13 7 13s7-8 7-13a7 7 0 00-7-7zm0 9.5a2.5 2.5 0 110-5 2.5 2.5 0 010 5z" fill="#fff"/></svg>&nbsp;48 Maple Row, USA</li>
    <li><svg width="12" height="10" viewBox="0 0 24 18"><path d="M1 1h22v16H1z" fill="#fff"/><path d="M1 1l11 8 11-8" stroke="#121212" stroke-width="2" fill="none"/></svg>&nbsp;support@brightoak.example</li>
    <li><svg width="12" height="12" viewBox="0 0 24 24"><path d="M6.6 10.8a15 15 0 006.6 6.6l2.2-2.2c.3-.3.7-.4 1-.2 1.1.4 2.3.6 3.6.6.6 0 1 .4 1 1V20c0 .6-.4 1-1 1A17 17 0 013 4c0-.6.4-1 1-1h3.5c.6 0 1 .4 1 1 0 1.3.2 2.5.6 3.6.1.3 0 .7-.2 1z" fill="#fff"/></svg>&nbsp;(+1) 555 014 7730</li>
  </ul>
</footer>

<div class="abs news">
  <h5 class="abs" style="left:37px;top:24px;font-size:14px;font-weight:500;color:#fff">Subscribe Newsletter</h5>
  <p class="abs" style="left:36px;top:44px;width:220px;font-size:12px;line-height:18px;color:#ccc">Sed ut perspiciatis unde omnis iste natus feria delavirot voluptatem accusantium.</p>
</div>
<div class="abs inp">Enter Your Email Address</div>
<div class="abs send"><svg width="20" height="20" viewBox="0 0 24 24"><path d="M4 3l17 9-17 9 3-9z" fill="#fff"/></svg></div>

<div class="abs copy">Copyright by Brightoak Renovations Co. All rights reserved.</div>

</body>
</html>
```